Briefpapier und Visitenkarten
Zielgruppe
In erster Linie mir selbst.
Aufgabenstellung
Gestaltung von Visitenkarten und Briefpapier.
Visitenkarten: Gestaltung beidseitig und in Pantone Farben
Briefpapier: Gestaltung einseitig und in Pantone Farben
Briefpapier und Visitenkarten sollen ein Design haben.

```html
<!DOCTYPE html>
<html lang="de">
<head>
<meta charset="utf-8">
<title>Korland Werbeagentur – Briefpapier und Visitenkarten</title>
<link href="https://fonts.googleapis.com/css2?family=Montserrat:wght@600&family=Questrial&display=swap" rel="stylesheet">
<style>
  :root {
    --ink: #1f2426;
    --label: #c2c2c2;
    --faint: #dadada;
    --mark: #c9c9c9;
    --paper: #ffffff;
    --stage: #ffffff;
    --edge: #d4d4d4;
  }
  html, body {
    margin: 0; padding: 0;
    width: 1200px; height: 900px;
    overflow: hidden;
    background: var(--stage);
    font-family: "Questrial", Arial, sans-serif;
    color: var(--ink);
  }
  .canvas { position: relative; width: 1200px; height: 900px; }
  .sheet {
    position: absolute;
    background: var(--paper);
    border: 1px solid var(--edge);
    box-shadow: 3px 4px 6px rgba(0,0,0,0.35);
    box-sizing: border-box;
    text-align: center;
  }
  .mark { position: absolute; border-radius: 50%; background: var(--mark); }
  .brand {
    position: absolute; left: 0; right: 0; white-space: nowrap;
    font-family: "Montserrat", Arial, sans-serif; font-weight: 600; letter-spacing: 0.03em;
  }
  .tagline { position: absolute; left: 0; right: 0; white-space: nowrap; text-transform: uppercase; color: var(--ink); }
  .label { color: var(--label); }

  /* Briefbogen */
  .letterhead { left: 21px; top: 9px; width: 621px; height: 876px; }
  .letterhead .mark { left: 292px; top: 35px; width: 38px; height: 38px; }
  .letterhead .brand { top: 76px; font-size: 12.5px; }
  .letterhead .tagline { top: 92px; font-size: 5px; letter-spacing: 0.45em; }
  .sender-line {
    position: absolute; left: 70px; top: 145px;
    font-size: 5.5px; color: var(--faint); text-transform: uppercase; letter-spacing: 0.03em;
  }
  .fold-mark { position: absolute; left: 0; top: 318px; width: 7px; height: 1px; background: var(--edge); }
  .footer {
    position: absolute; left: 0; right: 0; top: 816px;
    font-size: 7.8px; line-height: 10.3px; white-space: nowrap;
  }
  .footer .label { text-transform: uppercase; }

  /* Visitenkarten */
  .card { width: 479px; height: 312px; }
  .card-front { left: 689px; top: 218px; }
  .card-back { left: 687px; top: 562px; }
  .card .mark { left: 205px; top: 24px; width: 66px; height: 66px; }
  .card-front .brand { top: 97px; font-size: 23px; }
  .card-front .tagline { top: 127px; font-size: 9px; letter-spacing: 0.4em; }
  .card-back .brand {
    top: 91px; font-size: 26px; letter-spacing: 0.04em;
    font-family: "Questrial", Arial, sans-serif; font-weight: 400;
  }
  .role { position: absolute; left: 0; right: 0; top: 123px; font-size: 14px; letter-spacing: 0.07em; color: #555; }
  .contact { position: absolute; left: 0; right: 0; font-size: 15px; white-space: nowrap; }
  .card-front .address { top: 250px; font-size: 17.5px; letter-spacing: 0.04em; }
  .card-front .web { top: 273px; font-size: 16px; }
  .card-back .phone { top: 250px; font-size: 16px; }
  .card-back .online { top: 270px; }
  .gap { display: inline-block; width: 14px; }
</style>
</head>
<body>
<main class="canvas">

  <section class="sheet letterhead" aria-label="Briefbogen">
    <div class="mark" aria-hidden="true"></div>
    <div class="brand">KORLAND WERBEAGENTUR</div>
    <div class="tagline">Wir planen - Sie wachsen</div>
    <div class="sender-line">Korland Werbeagentur Lindenweg 14 D-50999 Feldhausen</div>
    <div class="fold-mark" aria-hidden="true"></div>
    <footer class="footer">
      <div><span class="label">Korland Werbeagentur</span> Wir planen - Sie wachsen</div>
      <div><span class="label">Geschäftsführer</span> Jonas Korland &nbsp;<span class="label">Lindenweg 14 &nbsp; D-50999 Feldhausen</span></div>
      <div><span class="label">Telefon</span> 02345.678 912 &nbsp; <span class="label">Fax</span> 02345.678 912 &nbsp; <span class="label">Email</span> korland@korlandwa.de &nbsp; <span class="label">Web</span> www.korlandwa.de</div>
      <div><span class="label">Stadtkasse Feldhausen</span> &nbsp;BLZ 200 300 40 &nbsp; KTO.: 98 765 432 &nbsp; <span class="label">UST-IDNR.</span> 987654321</div>
    </footer>
  </section>

  <section class="sheet card card-front" aria-label="Visitenkarte Vorderseite">
    <div class="mark" aria-hidden="true"></div>
    <div class="brand">KORLAND WERBEAGENTUR</div>
    <div class="tagline">Wir planen - Sie wachsen</div>
    <div class="contact address">LINDENWEG 14 &nbsp; D-50999 FELDHAUSEN</div>
    <div class="contact web"><span class="label">WEB</span> www.korlandwa.de</div>
  </section>

  <section class="sheet card card-back" aria-label="Visitenkarte Rückseite">
    <div class="mark" aria-hidden="true"></div>
    <div class="brand">JONAS KORLAND</div>
    <div class="role">GESCHÄFTSFÜHRER</div>
    <div class="contact phone"><span class="label">TELEFON</span> 02345.678 912<span class="gap"></span><span class="label">FAX</span> 02345.678 912</div>
    <div class="contact online"><span class="label">EMAIL</span> korland@korlandwa.de<span class="gap"></span><span class="label">WEB</span> www.korlandwa.de</div>
  </section>

</main>
</body>
</html>
```